Design some Business Cards for BWP

100% Guaranteed contest, check my history, perfect 5 star rating, I *always* select a winner and pay, even if we end up not using the winning design!!

Standard US size business cards, full color front and back.

Business cards for a company named : BWP (Brightmoor Wellness Partners)

The logo is attached, use similar color scheme.

Use following test information for the cards :

Perry Walsh
Owner
412 Elm Rd
Fairhaven, TX 76120
877-403-6190
info@[login to view URL]

NOTES:

1) If we see something we like we will close the project early so get your work in quick!
2) Before selecting the winner, we sort by date to ensure you have not stolen your concept from someone else (no cheating!).
3) Final hand off design to be in adobe illustrator format - no exceptions!
4) I cannot present your design to a client if it has your watermark on it. If you place a water mark your design, it will not be presented or win.

Good luck!

```html
<!DOCTYPE html>
<html lang="en">
<head>
<meta charset="utf-8">
<title>BWP Business Cards</title>
<link href="https://fonts.googleapis.com/css2?family=Tinos:wght@400;700&family=Montserrat:wght@400;500&display=swap" rel="stylesheet">
<style>
  :root {
    --stage: #ecebe8;
    --card-white: #ffffff;
    --blue: #1f86d6;
    --blue-deep: #0f5fb0;
    --blue-light: #63b6ee;
    --navy: #1d2a6e;
    --orange: #f5a21a;
    --orange-deep: #e9780f;
    --text-white: #ffffff;
  }
  * { margin: 0; padding: 0; box-sizing: border-box; }
  html, body { width: 1200px; height: 808px; overflow: hidden; }
  body { background: var(--stage); position: relative; }

  .card {
    position: absolute;
    left: 330px;
    width: 540px;
    height: 309px;
    background: var(--card-white);
    box-shadow: 0 6px 18px rgba(0,0,0,0.18);
    overflow: hidden;
  }
  .card--contact { top: 70px; }
  .card--front { top: 429px; }
  .card__art { position: absolute; inset: 0; width: 100%; height: 100%; }

  /* Contact side */
  .brand-lockup {
    position: absolute; left: 34px; top: 92px;
    display: flex; align-items: center; gap: 14px;
  }
  .brand-lockup__dot {
    width: 46px; height: 46px; border-radius: 50%;
    background: var(--blue-light);
  }
  .brand-lockup__name {
    font-family: "Tinos", serif; font-size: 58px; color: var(--navy); line-height: 1;
  }
  .brand-lockup__full {
    position: absolute; left: 36px; top: 160px;
    font-family: "Tinos", serif; font-size: 11px; color: var(--blue-deep);
    letter-spacing: 0.5px; text-transform: uppercase;
  }
  .contact {
    position: absolute; left: 318px; top: 74px;
    font-family: "Tinos", serif; color: var(--text-white);
    font-size: 15px; line-height: 1.35;
  }
  .contact__web { margin-bottom: 14px; }
  .contact__mark {
    position: absolute; right: 30px; top: 40px;
    width: 50px; height: 50px; border-radius: 50%;
    border: 4px solid var(--text-white);
  }

  /* Front side */
  .front__name {
    position: absolute; left: 48px; top: 62px;
    font-family: "Tinos", serif; font-size: 104px; color: var(--navy); line-height: 1;
  }
  .front__tagline {
    position: absolute; left: 40px; bottom: 30px;
    font-family: "Montserrat", sans-serif; font-size: 17px; color: var(--text-white);
    letter-spacing: 0.3px;
  }
  .front__mark {
    position: absolute; left: 400px; top: 120px;
    width: 100px; height: 100px; border-radius: 50%;
    background: var(--blue-light);
  }
</style>
</head>
<body>

<section class="card card--contact" aria-label="Business card, contact side">
  <svg class="card__art" viewBox="0 0 540 309" preserveAspectRatio="none" aria-hidden="true">
    <defs>
      <linearGradient id="contactBlue" x1="0" y1="0" x2="1" y2="1">
        <stop offset="0" stop-color="#0f5fb0"/>
        <stop offset="0.5" stop-color="#1f86d6"/>
        <stop offset="1" stop-color="#4aa8ea"/>
      </linearGradient>
    </defs>
    <path d="M240,0 C300,90 200,210 280,309 L540,309 L540,0 Z" fill="#f5a21a"/>
    <path d="M252,0 C312,90 212,210 292,309 L540,309 L540,0 Z" fill="url(#contactBlue)"/>
    <path d="M330,0 C380,100 300,220 380,309" fill="none" stroke="#63b6ee" stroke-opacity="0.35" stroke-width="2"/>
  </svg>

  <div class="brand-lockup">
    <span class="brand-lockup__dot"></span>
    <span class="brand-lockup__name">BWP</span>
  </div>
  <p class="brand-lockup__full">Brightmoor Wellness Partners</p>

  <div class="contact">
    <p>info@bwpcare.com</p>
    <p class="contact__web">www.bwpcare.com</p>
    <p>Perry Walsh</p>
    <p>Owner</p>
    <p>412 Elm Rd</p>
    <p>Fairhaven, TX 76120</p>
    <p>877-403-6190</p>
  </div>
  <span class="contact__mark"></span>
</section>

<section class="card card--front" aria-label="Business card, front side">
  <svg class="card__art" viewBox="0 0 540 309" preserveAspectRatio="none" aria-hidden="true">
    <defs>
      <linearGradient id="frontBlue" x1="0" y1="0" x2="1" y2="1">
        <stop offset="0" stop-color="#4aa8ea"/>
        <stop offset="0.55" stop-color="#1f86d6"/>
        <stop offset="1" stop-color="#0f5fb0"/>
      </linearGradient>
    </defs>
    <path d="M0,0 L380,0 C320,100 420,210 350,309 L0,309 Z" fill="#e9780f"/>
    <path d="M0,0 L366,0 C306,100 406,210 336,309 L0,309 Z" fill="#f5a21a"/>
    <path d="M0,0 L352,0 C292,100 392,210 322,309 L0,309 Z" fill="url(#frontBlue)"/>
    <path d="M180,0 C240,110 150,220 220,309" fill="none" stroke="#ffffff" stroke-opacity="0.15" stroke-width="3"/>
  </svg>

  <p class="front__name">BWP</p>
  <p class="front__tagline">Brightmoor Wellness Partners</p>
  <span class="front__mark"></span>
</section>

</body>
</html>
```